Brochure design for Veltrisa

Create a bi-fold A5 size brochure. I have attached our logo and the written content to be included in the brochure. So the brochure will have a total of 4 pages (front page, inner two pages, back page). End source files need to include final printable brochure as well as editable files.

```html
<!DOCTYPE html>
<html lang="en">
<head>
<meta charset="utf-8">
<title>Veltrisa bi-fold brochure</title>
<link rel="stylesheet" href="https://fonts.googleapis.com/css2?family=Lato:wght@300;400;700;900&family=Roboto+Condensed:wght@400;700&display=swap">
<style>
:root{
  --backdrop:#4a4a4c;
  --paper:#ffffff;
  --paper-grey:#f1f1f1;
  --blue:#1f73b8;
  --blue-deep:#0d68b1;
  --blue-light:#5aa3dc;
  --green:#8bc34a;
  --ink:#3e3e3e;
  --ink-soft:#5b5b5b;
}
*{margin:0;padding:0;box-sizing:border-box}
html,body{width:1200px;height:1200px;overflow:hidden;background:var(--backdrop)}
body{position:relative;font-family:"Roboto Condensed",sans-serif;color:var(--ink)}
.spread{position:absolute;left:234px;width:731px;height:518px;background:var(--paper);overflow:hidden}
.spread--outer{top:60px}
.spread--inner{top:621px}
.abs{position:absolute}
.fold-shade{position:absolute;top:0;left:326px;width:40px;height:100%;background:linear-gradient(90deg,rgba(0,0,0,0),rgba(0,0,0,.09));pointer-events:none}
.brand{position:absolute;display:flex;align-items:center;gap:6px}
.brand__dot{width:9px;height:9px;border-radius:50%;background:var(--green)}
.brand__name{font-family:"Lato",sans-serif;font-weight:700;font-size:21px;color:var(--blue);letter-spacing:.2px}
.refs{position:absolute;left:0;top:97px;width:366px;height:295px;background:linear-gradient(135deg,var(--blue-light),var(--blue) 70%);color:#fff;padding:27px 50px 0 50px}
.refs__lead{font-weight:700;font-size:7.4px;margin-bottom:10px}
.refs ul{list-style:none}
.refs li{font-size:5.1px;line-height:6.4px;margin-bottom:7px;padding-left:6px;position:relative}
.refs li::before{content:"";position:absolute;left:0;top:2px;width:3px;height:3px;border-radius:50%;background:#fff}
.refs__note{text-align:right;font-size:5.4px}
.contact-box{position:absolute;left:209px;top:367px;width:117px;height:131px;background:var(--green);color:#fff;padding:13px 8px;font-size:7.6px;line-height:12.4px}
.contact-box b{font-weight:700}
.avail{position:absolute;left:67px;top:427px;width:116px;font-size:7px;line-height:11.2px;color:var(--ink-soft);text-align:justify}
.photo{position:absolute}
.headline{position:absolute;left:548px;top:272px;width:147px;height:246px;background:var(--green);color:#fff;padding:16px 16px;font-family:"Lato",sans-serif;font-weight:300;font-size:16.2px;line-height:18.6px}
.headline b{font-weight:900}
.headline__punch{display:block;margin-top:12px;font-weight:900;font-size:18.6px;line-height:22px}
.page-right-bg{position:absolute;left:366px;top:0;width:365px;height:100%;background:var(--paper-grey)}
.section{position:absolute}
.section__title{font-family:"Lato",sans-serif;font-weight:300;font-size:14.6px;color:var(--blue);display:flex;align-items:center;gap:4px;white-space:nowrap}
.section__title b{font-weight:700}
.section__title::before{content:"";width:7px;height:7px;border:1.8px solid var(--green);flex:none}
.section p{font-size:7.1px;line-height:11.3px;text-align:justify;color:var(--ink-soft)}
.section--left p{margin-left:12px;width:287px}
.section--col p{margin-left:14px;width:137px}
.web-tab{position:absolute;left:387px;top:0;width:117px;height:61px;background:var(--green);color:#fff;font-weight:700;font-size:8px;line-height:12.6px;padding:18px 0 0 21px}
.band{position:absolute;left:366px;top:330px;width:365px;height:167px;background:var(--blue-deep)}
.band p{position:absolute;top:11px;width:137px;font-size:7.1px;line-height:11.3px;text-align:justify;color:#fff}
</style>
</head>
<body>

<section class="spread spread--outer" aria-label="Back and front covers">
  <div class="brand" style="left:147px;top:42px"><span class="brand__dot"></span><span class="brand__name">Veltrisa</span></div>
  <div class="brand" style="left:591px;top:42px"><span class="brand__dot"></span><span class="brand__name">Veltrisa</span></div>

  <div class="refs">
    <p class="refs__lead">For a list of approved VeltrisaTM retailers please visit www.veltrisa.co</p>
    <ul>
      <li>2003 Release: International Consortium Completes HGP. Available at: https://www.example-genome.org/2003-consortium-release</li>
      <li>Marlow TJ, Ostend P, Quill R: Clinical application of pharmacogenetics. Trends Mol. Med.7 (2001).</li>
      <li>Harlen K, et al. Pharmacogenetics 1998;8:283-289.</li>
      <li>Lio T, et al. Journal of Molecular Diagnostics 2016;18(3):438-45.</li>
      <li>Brask W, et al. Clinical Pharmacology and Therapeutics 2016;100(2):160-9.</li>
      <li>Denholm N, et al. Pharmacogenomics and Personalized Medicine 2017;27(10):17-27.</li>
      <li>Varrow S, et al. Clinical Pharmacology and Therapeutics 2014;95(4):423-31.</li>
      <li>Aldine W, et al. Food elimination based on IgG antibodies in irritable bowel syndrome: a randomised controlled trial. Gut 53 (2004).</li>
      <li>Mercer N, et al. Randomised controlled trial of food elimination diet based IgG antibodies for the prevention of migraine like headaches. Nutrition Journal 10 (2011).</li>
      <li>Orlen M, Pasco R, Tiller H. Food allergy mediated by IgG antibodies associated with migraine in adults. Allergy Review 54 (2007).</li>
      <li>Corvi C, Falden F, Alto F. Immune complexes in food-induced arthralgia. Ann Allergy 59 (1987).</li>
    </ul>
    <p class="refs__note">* Additional fees may apply.</p>
  </div>

  <p class="avail">Please note test availability may differ from region to region and is subject to availability. Please talk to your local retailer for more information</p>

  <div class="contact-box">For more information about VeltrisaTM or our products, please talk to your local retailer or email us at enquiries@<br><b>www.veltrisa.co<br>info@veltrisa.co</b></div>

  <svg class="photo" style="left:366px;top:97px" width="345" height="295" role="img" aria-label="Laboratory photo: pipette dispensing liquid into a well plate">
    <defs><linearGradient id="lab" x1="0" y1="0" x2="1" y2="1">
      <stop offset="0" stop-color="#eef1f4"/><stop offset=".45" stop-color="#b9d6da"/><stop offset=".75" stop-color="#6fb3bb"/><stop offset="1" stop-color="#dfe6ea"/>
    </linearGradient></defs>
    <rect width="345" height="295" fill="url(#lab)"/>
  </svg>

  <div class="headline">A REVOLUTION IN <b>HEALTH &amp; WELLNESS</b> HAS BEEN BREWING AND<span class="headline__punch">NOW IT<br>IS HERE!</span></div>
  <div class="fold-shade"></div>
</section>

<section class="spread spread--inner" aria-label="Inside spread">
  <div class="page-right-bg"></div>

  <div class="section section--left" style="left:39px;top:52px">
    <h2 class="section__title">PRECISION <b>HEALTH &amp; WELLNESS</b></h2>
    <p>You are unique. Your healthcare and lifestyle decisions need to be tailored to you. Ever since the human genome was decoded, a plethora of scientific data has revealed everything from disease-causing genes to genetically tailored diets. We all want to live longer and healthier lives, whilst performing at out peak. One size does not fit all and the only way to find out what's right for you is to unlock your hidden code.</p>
  </div>
  <div class="section section--left" style="left:39px;top:146px">
    <h2 class="section__title">DNA THE <b>CODE OF LIFE</b></h2>
    <p>Every individual living organism has a completely unique set of DNA. Your DNA is the chemical blueprint that codes for everything in your body and is found in all of the trillions of cells that you are made of. Collections of DNA are called genes and the complete set of genes in an individual is referred to as their genome. The human genome was first decoded in 2003, taking over 13 years and $2.7 billion to complete1. Thanks to exponential advances in technology, VeltrisaTM can now unlock your DNA for only a fraction of the time and cost.</p>
  </div>
  <div class="section section--left" style="left:39px;top:253px">
    <h2 class="section__title">UNLOCK <b>YOUR HIDDEN CODE</b></h2>
    <p>A whole new world of discovery awaits with the VeltrisaTM range of genetic testing services. From unlocking your complete genome with Whole Genome Sequencing (WGS) to just learning about specific aspects of what makes you… you. With VeltrisaTM, you can find answers to the questions that can help you to live a healthier, longer and optimal quality of life.</p>
  </div>

  <svg class="photo" style="left:38px;top:330px" width="328" height="167" role="img" aria-label="Illustration of a glowing DNA double helix in blue and green">
    <defs><linearGradient id="helix" x1="0" y1="0" x2="1" y2="1">
      <stop offset="0" stop-color="#7fc8d6"/><stop offset=".5" stop-color="#2fa6a0"/><stop offset="1" stop-color="#7ccf6a"/>
    </linearGradient></defs>
    <rect width="328" height="167" fill="url(#helix)"/>
  </svg>

  <div class="web-tab">www.veltrisa.co<br>info@veltrisa.co</div>

  <div class="section section--col" style="left:381px;top:95px">
    <h2 class="section__title">DNA &amp; <b>DISEASE</b></h2>
    <p style="margin-top:6px">Prevention is better than any cure. Scientific studies have uncovered numerous genes associated with a range of cancers, heart conditions, and other common diseases affecting society today. The range of genetic tests available through VeltrisaTM can now identify if these, and other, genes are present in you. This allows you and your physician to potentially prevent, manage, monitor and treat relevant conditions. Furthermore, as the rapid pace of science continues to uncover new genes related to disease, VeltrisaTM can quickly update you and your doctor with the latest research and what it means for you*.</p>
  </div>
  <div class="section section--col" style="left:549px;top:57px">
    <h2 class="section__title">DNA &amp; <b>DRUGS</b></h2>
    <p style="margin-top:4px">Scientific research has shown that the response rate for many prescribed drugs is as low as 50% and that genetic factors can account for up to 95% of drug-response variability and susceptibility.2-3 In other words, many of the drugs you take in your lifetime will likely be inadequately dosed, leading to potential side effects or no effects at all. With VeltrisaTM, you and your doctor can proactively identify appropriate types, and dosages, for a range of prescribed and over-the-counter medications. This includes medications you currently take and any commons future medications you are likely to encounter at some stage in your life. A number of studies have shown that over 74% of people taking a genetic test for medication compatibility learned information that is relevant to them.4-7</p>
  </div>
  <div class="section" style="left:381px;top:306px"><h2 class="section__title">DNA &amp; <b>DIET</b></h2></div>
  <div class="section" style="left:549px;top:306px"><h2 class="section__title">DNA &amp; <b>DESCENT</b></h2></div>

  <div class="band">
    <p style="left:30px">Certain foods are thought to inappropriately cause immune reactions in genetically predisposed individuals. This can result in symptoms like fatigue, bloating, bowel disturbances, headaches, migraines, joint aches, eczema or acne8-11. DNA testing can help identify such foods as well as genes associated with the metabolism and absorption of vitamins, minerals and stimulants like coffee. The VeltrisaTM range of tests can even help create precision diet and fitness plans based on your genes and goals.</p>
    <p style="left:198px">The discipline of genealogy has exploded over recent years with the advent of DNA testing. The VeltrisaTM range of tests can help you track and understand your ancestry and paternity tests can help identify an individual's biological father. Family planning tests can help identify a couple's risk profile for conceiving children with any of the dozens of known genetic conditions that can affect humans.</p>
  </div>
  <div class="fold-shade"></div>
</section>

</body>
</html>
```